Postcard double sided

Title: DWIGHT'S REVENGE

Why would Dwight Kessler align himself with Gordon Pruett?

(photo of two guys)

Dwight approached elected officials that he wanted to run for office, but did not have money to finance his campaign. He wanted other elected officials to finance his campaign. Everyone told him that they would help him get the vote out, but that he needed to finance his own race.

In comes Gordon Pruett.

Gordon Pruett who has a pay to play scheme over at the City, told Dwight he would finance his campaign on one condition.

He needed to run against Steven Hulse.

Why would Dwight want to run with no money?

Backside

DWIGHT'S REVENGE

Dwight decided to run because no one on the school board would terminate Dwight's ex and her new boyfriend who both work for the school district. His ex even filed criminal charges against him that are still pending.

Mug Shot facing left (name the charges Criminal Trespass , and Criminal Mischief (highlight bold letters use two lines) mug shot facing right

Complaint one (then photo with full face) Compliant 2)
(showcharges)

Dwight's ultimate goal is to terminate his ex and her new boyfriend if elected.
Plus Gordon Pruett needs the majority on the school board to do what he does bet.

Kickbacks for Contracts.

They will hire their own contractors!
Say "No" to Dwight's Revenge and Gordon Pruett Money Grab!

Title On Back: all caps: DOMESTIC VIOLENCE

```html
<!DOCTYPE html>
<html lang="en">
<head>
<meta charset="UTF-8">
<title>Dwight's Revenge – Postcard</title>
<link href="https://fonts.googleapis.com/css2?family=Lato:wght@400;700;900&display=swap" rel="stylesheet">
<style>
  :root{
    --navy:#26379b;
    --sky:#22a5e2;
    --paper:#ffffff;
    --stage:#2b2b2d;
    --ink-dark:#2a2f45;
    --ink-muted:#4a4f63;
  }
  *{box-sizing:border-box;margin:0;padding:0}
  html,body{width:1200px;height:776px;overflow:hidden}
  body{background:var(--stage);font-family:'Lato',sans-serif;position:relative}
  .card{position:absolute;top:24px;width:520px;height:728px;background:var(--paper);overflow:hidden}
  .card--front{left:60px}
  .card--back{left:620px}
  .card__art{position:absolute;inset:0}

  /* front */
  .front-text{position:absolute;left:30px;top:338px;color:var(--navy)}
  .front-title{font-weight:900;font-size:46px;line-height:1;letter-spacing:.3px;padding-bottom:8px;border-bottom:3px solid var(--navy);width:262px}
  .front-subtitle{font-weight:400;font-size:17px;line-height:1.2;margin-top:8px;color:var(--ink-dark);padding-bottom:8px;border-bottom:3px solid var(--navy);width:300px}
  .front-body{font-size:10.5px;line-height:1.3;margin-top:7px;padding-bottom:7px;border-bottom:3px solid var(--navy);width:330px}
  .front-cols{display:flex;margin-top:9px;width:370px}
  .front-cols__left{flex:0 0 200px;text-align:right;padding-right:8px;font-size:10px;line-height:1.3;color:var(--ink-muted);border-right:2px solid var(--navy)}
  .front-cols__left strong{color:#1f2233;font-weight:700}
  .front-cols__right{padding-left:8px;font-size:10px;line-height:1.2;text-transform:uppercase;color:var(--navy)}
  .front-cols__right p:first-child{padding-bottom:4px;border-bottom:1.5px solid var(--navy);margin-bottom:5px}
  .front-cols__right p:last-child{font-weight:700}

  /* back */
  .back-content{position:absolute;inset:0;text-align:center}
  .back-title{color:#fff;font-weight:700;font-size:21px;letter-spacing:.5px;margin-top:42px}
  .back-copy{color:#fff;font-size:11px;line-height:1.3;width:400px;margin:12px auto 0}
  .back-note{color:#fff;font-size:11px;line-height:1.3;width:400px;margin:20px auto 0}
  .complaint-title{color:#fff;font-weight:700;font-size:23px;letter-spacing:.5px;margin-top:40px}
  .mugshots{display:flex;justify-content:center;gap:10px;margin-top:18px}
  .mugshot{width:132px;height:158px;border-radius:14px;border:2px solid #d7d9e2;background:linear-gradient(180deg,#8a8d92 0%,#6f7276 60%,#2f4a35 100%)}
  .back-goal{color:var(--navy);font-size:11px;line-height:1.3;width:440px;margin:26px auto 0}
  .back-headline{color:var(--navy);font-weight:900;font-size:27px;letter-spacing:.3px;margin-top:12px}
  .back-cta{color:var(--navy);font-size:11px;line-height:1.35;margin-top:10px}
  .back-footer{color:var(--navy);font-weight:900;font-size:28px;letter-spacing:.3px;margin-top:16px}
</style>
</head>
<body>

<section class="card card--front">
  <svg class="card__art" width="520" height="728" viewBox="0 0 520 728">
    <defs>
      <linearGradient id="photoTone" x1="0" y1="0" x2="0" y2="1">
        <stop offset="0" stop-color="#3a4f8e"/>
        <stop offset=".5" stop-color="#4a4f5c"/>
        <stop offset="1" stop-color="#1e2230"/>
      </linearGradient>
      <clipPath id="photoCut"><rect x="0" y="0" width="520" height="575"/></clipPath>
    </defs>
    <path d="M100,0 C110,150 180,230 250,330 C320,430 420,560 520,700 L560,760 L560,0 Z" fill="var(--navy)"/>
    <path d="M114,0 C124,150 194,230 264,330 C334,430 434,560 534,700 L574,760 L574,0 Z" fill="var(--sky)"/>
    <path d="M128,0 C138,150 208,230 278,330 C348,430 448,560 548,700 L588,760 L588,0 Z" fill="var(--paper)"/>
    <path clip-path="url(#photoCut)" d="M128,0 C138,150 208,230 278,330 C348,430 448,560 548,700 L588,760 L588,0 Z" fill="url(#photoTone)" role="img" aria-label="Photo of Dwight Kessler and Gordon Pruett standing together in suits in front of a campaign backdrop"/>
  </svg>

  <div class="front-text">
    <h1 class="front-title">DWIGHT'S<br>REVENGE</h1>
    <h2 class="front-subtitle">Why would Dwight Kessler align himself with Gordon Pruett?</h2>
    <p class="front-body">Dwight approached elected officials that he wanted to run for office, but did not have money to finance his campaign. He wanted other elected officials to finance his campaign. Everyone told him that they would help him get the vote out, but that he needed to finance his own race.</p>
    <div class="front-cols">
      <div class="front-cols__left">
        <p><strong>In comes Gordon Pruett.</strong></p>
        <p>Gordon Pruett who has a pay to play scheme over at the City, told Dwight he would finance his campaign on one condition.</p>
      </div>
      <div class="front-cols__right">
        <p>He needed to run against Steven Hulse.</p>
        <p>Why would Dwight want to run with no money?</p>
      </div>
    </div>
  </div>
</section>

<section class="card card--back">
  <svg class="card__art" width="520" height="728" viewBox="0 0 520 728">
    <path d="M0,0 H520 V392 H210 C110,392 30,300 0,90 Z" fill="var(--navy)"/>
  </svg>
  <div class="back-content">
    <h2 class="back-title">DWIGHT'S REVENGE</h2>
    <p class="back-copy">Dwight decided to run because no one on the school board would terminate Dwight's ex and her new boyfriend who both work for the school district. His ex even filed criminal charges against him that are still pending.</p>
    <p class="back-note">Mug Shot facing left (name the charges Criminal Trespass , and Criminal Mischief (highlight bold letters use two lines) mug shot facing right</p>
    <h3 class="complaint-title">COMPLAINT ONE</h3>
    <div class="mugshots">
      <div class="mugshot" role="img" aria-label="Booking photo, profile facing left"></div>
      <div class="mugshot" role="img" aria-label="Booking photo, facing front"></div>
      <div class="mugshot" role="img" aria-label="Booking photo, profile facing right"></div>
    </div>
    <p class="back-goal">Dwight's ultimate goal is to terminate his ex and her new boyfriend if elected. Plus Gordon Pruett needs the majority on the school board to do what he does bet.</p>
    <h3 class="back-headline">KICKBACKS FOR CONTRACTS.</h3>
    <p class="back-cta">They will hire their own contractors!<br>Say "No" to Dwight's Revenge and Gordon Pruett Money Grab!</p>
    <h3 class="back-footer">DOMESTIC VIOLENCE</h3>
  </div>
</section>

</body>
</html>
```